Beautiful Customer Appreciation Gift Box Need Eye Catching Brochure

I need a brochure to include with small sample gift boxes that I send or give to companies who do door to door marketing of businesses, company reps, real estate designers and large companies looking for a unique customer appreciation gifts.

The brochure needs to capture the size variations and the limitless options for their budget and customization needs.

They are gift boxes that can be filled with cookies for the drug rep making an impression for the doc - after cookies are gone, the gift remains

At christmas, we fill them with baked goods and provide to each office. Every year as i visit the offices, they have last years gift box out as a decoration.

realtors can use them as a welcome to your new home gift filled with a bottle of wine and their papers left on the kitchen counter

We have had them used for baby shower gifts, kept later as a decoration.

that's the concept, i need it captured.
Marlow's Festive Nook is the current name
a tag line we came up with is It's all in the WRAPPINGS.
Updates

Project Deadline Extended
Reason: We are very close, I have my photoshoot tomorrow and I'd like to see and continue to tweek the current designs. I have pretty well deleted the designs we are not considering at this point. The others all have components we love. So I need a little more time and some tweaking to decide for sure.

Target Market(s)

the target is the company or individuals looking for gift giving options for clients and customers. From the door to door salesperson looking to make a splash or big impression to the large company looking for nice corporate gift ideas.

The concept of say goodbye to plain jane gift boxes that all look alike... Say goodbye to expensive gift wrap and bows that get thrown away in minutes.... and hello to a beautiful custom made gift box that will remain a decoration or keepsake box forever....

Industry/Entity Type

Retail

Font styles to use
Sans Serif
Script

Requirements
Must have
• IMPORTANT... I CAN and AM GETTING better pictures for the printing purposes. I'm looking more for the concept of the brochuure and layout design.
• I'd love to have it have some place holders for various pictures and descriptions - because each industry targets different people, I'd like to be able to change the front cover of the brochure with a picture of a box that targets that audience a little.
• For a real estate person... i might choose a beautiful centerpiece looking one... vs, the ob/gyn office, I might choose a baby one.
• I have some design skill, just 0 times and the programs have changed alot over the years, so this may go on to future work and a long design relationship as the company grows and changes. I do know photoshop and pagemaker from long ago so I should be able to drop in pics and text options. if we use compatible programs.
Nice to have
• would love to have some kind of background for the page - not just plain white background.
• i like angles and curves
Should not have
• boxy look.

```html
<!DOCTYPE html>
<html lang="en">
<head>
<meta charset="utf-8">
<title>Marlow's Festive Nook – Trifold Brochure</title>
<link rel="stylesheet" href="https://fonts.googleapis.com/css2?family=Oswald:wght@500;600&family=Roboto:wght@400;500&display=swap">
<style>
  :root {
    --page-bg: #2b2b2d;
    --pink: #ef6ce6;
    --pink-bright: #f25ae8;
    --blue-deep: #0a36c4;
    --blue-mid: #1450e6;
    --blue-light: #2f7bf5;
    --white: #ffffff;
    --ink: #2a2030;
  }
  * { box-sizing: border-box; margin: 0; padding: 0; }
  html, body { width: 1200px; height: 947px; overflow: hidden; }
  body { background: var(--page-bg); position: relative; }

  .brochure {
    position: absolute; left: 60px; top: 52px;
    width: 1080px; height: 842px;
    display: grid; grid-template-columns: repeat(3, 360px);
  }
  .panel { position: relative; width: 360px; height: 842px; overflow: hidden; }
  .panel-bg { position: absolute; inset: 0; width: 100%; height: 100%; display: block; }

  /* About panel */
  .about { background: var(--pink); }
  .about-photo {
    position: absolute; left: 0; top: 0; width: 100%; height: 370px;
    background:
      radial-gradient(circle at 30% 30%, #d9d4c8 0 12%, transparent 30%),
      radial-gradient(circle at 70% 65%, #8a6fc8 0 14%, transparent 32%),
      radial-gradient(circle at 75% 20%, #b84040 0 8%, transparent 22%),
      linear-gradient(135deg, #5b6a3a, #8a7a5a 45%, #6e5a7e);
  }
  .about-photo::after {
    content: ""; position: absolute; left: 0; right: 0; bottom: 0; height: 80px;
    background: linear-gradient(to bottom, rgba(239,108,230,0), var(--pink));
  }
  .about-title {
    position: absolute; top: 398px; left: 0; width: 100%; text-align: center;
    font-family: "Roboto", sans-serif; font-weight: 500; font-size: 25px;
    color: var(--white); letter-spacing: 0.5px;
  }
  .about-body {
    position: absolute; top: 450px; left: 44px; width: 288px;
    font-family: "Roboto", sans-serif; font-size: 16.5px; line-height: 21.5px;
    color: var(--ink); text-align: justify;
  }

  /* Contact panel */
  .contact-text {
    position: absolute; left: 0; width: 100%; text-align: center;
    font-family: "Roboto", sans-serif; font-weight: 500; color: var(--white);
  }
  .call-label { top: 676px; font-size: 20px; }
  .call-number { top: 702px; font-size: 38px; letter-spacing: 1px; }
  .web-address { top: 774px; font-size: 25px; }

  /* Cover panel */
  .brand-frame {
    position: absolute; top: 50px; left: 20px; width: 290px; height: 50px;
    border: 2px solid var(--white);
    display: flex; align-items: center; justify-content: center;
    font-family: "Oswald", sans-serif; font-weight: 500; font-size: 23px;
    color: var(--white); letter-spacing: 0.5px;
  }
  .cover-headline {
    position: absolute; top: 122px; left: 20px; width: 280px;
    font-family: "Oswald", sans-serif; font-weight: 600; font-size: 46px;
    line-height: 62px; color: var(--white);
  }
  .cover-sub {
    position: absolute; top: 256px; left: 20px;
    font-family: "Oswald", sans-serif; font-weight: 600; font-size: 22px;
    color: var(--pink-bright); letter-spacing: 0.3px;
  }
</style>
</head>
<body>
  <main class="brochure">
    <section class="panel about">
      <div class="about-photo" role="img" aria-label="Photo of several decorated gift boxes filled with silk flowers on a table"></div>
      <h2 class="about-title">ABOUT US</h2>
      <p class="about-body">Marlow's Festive Nook creates custom gift boxes for sales reps, realtors and companies who want to be remembered. Fill one with cookies for the doctor's office, baked goods at Christmas, or wine as a welcome to a new home. Every size and budget can be matched to your theme. Say goodbye to plain boxes and wrapping paper thrown away in minutes. When the treats are gone, the gift remains as a keepsake.</p>
    </section>

    <section class="panel contact">
      <svg class="panel-bg" viewBox="0 0 360 842">
        <defs>
          <linearGradient id="contactBlue" x1="0" y1="0" x2="1" y2="0">
            <stop offset="0" stop-color="#0a36c4"/>
            <stop offset="0.6" stop-color="#1450e6"/>
            <stop offset="1" stop-color="#0b3fd2"/>
          </linearGradient>
          <linearGradient id="boxPink" x1="0" y1="0" x2="1" y2="1">
            <stop offset="0" stop-color="#e8b8c8"/><stop offset="1" stop-color="#8a6a5a"/>
          </linearGradient>
          <linearGradient id="boxBlue" x1="0" y1="0" x2="1" y2="1">
            <stop offset="0" stop-color="#6fa6c8"/><stop offset="1" stop-color="#6a5a3a"/>
          </linearGradient>
          <linearGradient id="boxGreen" x1="0" y1="0" x2="1" y2="1">
            <stop offset="0" stop-color="#8aa05a"/><stop offset="1" stop-color="#5a4a3a"/>
          </linearGradient>
        </defs>
        <rect width="360" height="842" fill="url(#contactBlue)"/>
        <path d="M12 0 C 40 200, 200 420, 372 600" fill="none" stroke="var(--pink)" stroke-width="18"/>
        <path d="M6 0 C 34 200, 194 420, 366 600" fill="none" stroke="var(--white)" stroke-width="9"/>
        <circle cx="86" cy="145" r="84" fill="var(--white)"/>
        <g role="img" aria-label="Photo of a pink floral gift box"><circle cx="86" cy="145" r="74" fill="url(#boxPink)"/></g>
        <circle cx="152" cy="320" r="84" fill="var(--white)"/>
        <g role="img" aria-label="Photo of a blue daisy gift box arrangement"><circle cx="152" cy="320" r="74" fill="url(#boxBlue)"/></g>
        <circle cx="255" cy="505" r="84" fill="var(--white)"/>
        <g role="img" aria-label="Photo of a green garden gift box"><circle cx="255" cy="505" r="74" fill="url(#boxGreen)"/></g>
      </svg>
      <p class="contact-text call-label">CALL NOW</p>
      <p class="contact-text call-number">XXXXXXXXXX</p>
      <p class="contact-text web-address">marlowsfestivenook.com</p>
    </section>

    <section class="panel cover">
      <svg class="panel-bg" viewBox="0 0 360 842">
        <defs>
          <linearGradient id="coverBlue" x1="0" y1="0" x2="1" y2="1">
            <stop offset="0" stop-color="#1a5af0"/>
            <stop offset="0.5" stop-color="#2f7bf5"/>
            <stop offset="1" stop-color="#0a36c4"/>
          </linearGradient>
          <radialGradient id="flowerFill" cx="0.5" cy="0.5" r="0.6">
            <stop offset="0" stop-color="#f4f0f6"/>
            <stop offset="0.45" stop-color="#9a6ad8"/>
            <stop offset="1" stop-color="#5a3aa0"/>
          </radialGradient>
          <clipPath id="coverCircle"><circle cx="262" cy="620" r="160"/></clipPath>
        </defs>
        <rect width="360" height="842" fill="url(#coverBlue)"/>
        <path d="M360 0 C 345 230, 300 290, 200 410 C 95 535, 12 665, 6 842 L 360 842 Z" fill="var(--pink)"/>
        <path d="M360 0 C 345 230, 300 290, 200 410 C 95 535, 12 665, 6 842" fill="none" stroke="var(--white)" stroke-width="9"/>
        <path d="M348 0 C 333 230, 288 290, 188 410 C 83 535, 0 665, -6 842" fill="none" stroke="var(--blue-deep)" stroke-width="4"/>
        <circle cx="262" cy="620" r="160" fill="var(--white)"/>
        <g role="img" aria-label="Photo of a purple and white floral centerpiece gift box" clip-path="url(#coverCircle)">
          <rect x="110" y="520" width="260" height="330" rx="120" fill="url(#flowerFill)"/>
        </g>
      </svg>
      <div class="brand-frame">MARLOW'S FESTIVE NOOK</div>
      <h1 class="cover-headline">GIFT BOXES<br>THAT REMAIN</h1>
      <p class="cover-sub">IT'S ALL IN THE WRAPPINGS.</p>
    </section>
  </main>
</body>
</html>
```